International Supplier needs an eye catching profssional letterhead and continuation page

We need a letterhead and continuation sheet designed for a company based in Austria called VULMA Screens GmbH. We develop and install innovate glass partition wall solutions to commercial and cultural buildings and to some of the most contemporary architectural buildings in Europe. I have our inhouse design brief confirming our corporate colours, fonts and images and have our corporate logo available in a variety of formats including AI and EPS. We are open to differing design suggestions as long as they follow the colour and font specification in our corporate design brief. We are at the forefront of innovation, craftmanship and design for architectural glass, framing systems and fire rated partition systems. The final design should communicate the spirit and strength of the company.
www.vulma.com / www.parvoline.co.uk / www.emberpane.com

Target Market(s)

Architects, planners, designers, building contractors and construction companies

Industry/Entity Type

Architecture

Font styles to use
Sans Serif

Requirements
Must have
• VULMA Screens GmbH
• Lindorferweg 14 B
• 7041 Marnfeld
• Österreich
• Tel: +43 (1) 482 6170
• E-mail:office@vulmascreens.at
• Web:www.vulmascreens.at / www.vulmaemberpane.com
• subtle yet professionally distinctive
• colours and fonts to be taken ffom VULMA design guide but we are also open to variations on the same theme
Should not have
• No bold lines

```html
<!DOCTYPE html>
<html lang="en">
<head>
<meta charset="utf-8">
<title>VULMA Screens GmbH – Letterhead</title>
<link href="https://fonts.googleapis.com/css2?family=Lato:wght@400;700&display=swap" rel="stylesheet">
<style>
  :root {
    --brand: #c8345a;
    --ink: #3d3d40;
    --body: #6e6e6e;
    --paper: #f6f5ee;
    --backdrop: #e6e4df;
  }
  * { margin: 0; padding: 0; box-sizing: border-box; }
  html, body {
    width: 1158px; height: 1200px; overflow: hidden;
    background: var(--backdrop);
    font-family: "Lato", sans-serif;
  }
  .sheet {
    position: absolute; left: 142px; top: 20px;
    width: 873px; height: 1160px;
    background: var(--paper);
    box-shadow: 0 2px 10px rgba(0,0,0,.12);
    overflow: hidden;
  }
  .header-shape, .footer-shape { position: absolute; left: 0; top: 0; }
  .brand {
    position: absolute; left: 88px; top: 76px;
    display: flex; align-items: center; gap: 10px;
  }
  .brand-mark { width: 42px; height: 42px; background: var(--brand); }
  .brand-name {
    font-size: 54px; font-weight: 400; color: var(--ink);
    letter-spacing: 0; line-height: 1;
  }
  .contact {
    position: absolute; left: 580px; top: 49px;
    list-style: none; color: #fff; font-size: 9.5px; line-height: 15.3px;
  }
  .contact li { display: flex; align-items: center; gap: 6px; }
  .contact svg { width: 9px; height: 9px; flex: none; }
  .recipient { position: absolute; left: 108px; top: 264px; color: var(--ink); }
  .recipient .salutation { font-size: 13px; font-weight: 700; }
  .recipient .designation { font-size: 9px; color: var(--body); }
  .recipient .company { font-size: 13px; font-weight: 700; }
  .date {
    position: absolute; right: 99px; top: 293px;
    font-size: 13px; font-weight: 700; color: var(--ink);
  }
  .letter-body {
    position: absolute; left: 103px; top: 380px; width: 679px;
    font-size: 13.4px; line-height: 16.5px; color: var(--body);
    letter-spacing: 0.9px; word-spacing: 0.5px;
    text-align: justify;
  }
  .letter-body p { margin-bottom: 10px; }
  .letter-body p.lead { font-weight: 700; color: #555; letter-spacing: 0.45px; margin-top: 22px; margin-bottom: 12px; }
  .letter-body p.closing { margin-top: 18px; }
  .signature {
    position: absolute; left: 647px; top: 930px; width: 126px; height: 30px;
    background: linear-gradient(90deg, rgba(61,61,64,.06), rgba(61,61,64,.14));
    border-bottom: 1px solid var(--ink);
  }
  .signatory { position: absolute; right: 99px; top: 979px; text-align: right; }
  .signatory .name { font-size: 15px; font-weight: 700; color: var(--brand); letter-spacing: .5px; }
  .signatory .role { font-size: 11.5px; color: var(--ink); margin-top: 2px; }
</style>
</head>
<body>
  <main class="sheet">
    <svg class="header-shape" width="873" height="175" viewBox="0 0 873 175" aria-hidden="true">
      <polygon points="419,0 873,0 873,174 602,174" fill="var(--brand)"/>
    </svg>

    <div class="brand">
      <span class="brand-mark"></span>
      <span class="brand-name">VULMA</span>
    </div>

    <ul class="contact">
      <li><svg viewBox="0 0 10 10"><path d="M2 1l2 2-1 1.2c.6 1.2 1.5 2.1 2.8 2.8L7 6l2 2-1.3 1.3C4.5 9 1 5.5.7 2.3z" fill="#fff"/></svg>+43 (1) 482 6170</li>
      <li><svg viewBox="0 0 10 10"><rect x="0.5" y="2" width="9" height="6" fill="#fff"/><path d="M.5 2l4.5 3.5L9.5 2" stroke="var(--brand)" stroke-width=".8" fill="none"/></svg>office@vulmascreens.at</li>
      <li><svg viewBox="0 0 10 10"><circle cx="5" cy="5" r="4.2" fill="none" stroke="#fff" stroke-width="1"/><path d="M1 5h8M5 1c-2 2.5-2 5.5 0 8M5 1c2 2.5 2 5.5 0 8" stroke="#fff" stroke-width=".8" fill="none"/></svg>www.vulmascreens.at / www.vulmaemberpane.com</li>
      <li><svg viewBox="0 0 10 10"><path d="M5 .5a3.2 3.2 0 0 1 3.2 3.2C8.2 6 5 9.5 5 9.5S1.8 6 1.8 3.7A3.2 3.2 0 0 1 5 .5z" fill="#fff"/><circle cx="5" cy="3.7" r="1.1" fill="var(--brand)"/></svg>Lindorferweg 14 B A 7041 Marnfeld Österreich</li>
    </ul>

    <div class="recipient">
      <p class="salutation">Dear, Mr________</p>
      <p class="designation">Designation</p>
      <p class="company">Company Name</p>
    </div>
    <p class="date">DATE:08/02/2018</p>

    <section class="letter-body">
      <p>Lorem Ipsum is simply dummy text of the printing and typesetting industry. Lorem Ipsum has been the industry's standard dummy text ever since the1500s,when an unknown printer took a galley of type and scrambled it to make a type specimen book. It has survived not only five centuries, but also the leap into electronic typesetting, remaining essentially unchanged. It was popularised in the 1960s with the release of Veltrafix sheets containing Lorem Ipsum passages,and more recently with desktop publishing software like Orvel PageForm including versions of Lorem Ipsum.</p>
      <p>Lorem Ipsum is simply dummy text of the printing and typesetting industry. Lorem Ipsum has been the industry's standard dummy text ever since the1500s,when an unknown printer took a galley of type and scrambled it to make a type specimen book. It has survived not only five centuries, but also the leap into electronic typesetting, remaining essentially unchanged. It was popularised in the 1960s with the release of Veltrafix sheets containing Lorem Ipsum passages,and more recently with desktop publishing software like Orvel PageForm including versions of Lorem Ipsum.</p>
      <p class="lead">Lorem Ipsum is simply dummy text of the printing and typesetting industry. Lorem Ipsum has been the industry's standard dummy text ever since the1500s,when an unknown printer took a galley of type and scrambled it to make a type specimen book.</p>
      <p>Lorem Ipsum is simply dummy text of the printing and typesetting industry. Lorem Ipsum has been the industry's standard dummy text ever since the1500s,when an unknown printer took a galley of type and scrambled it to make a type specimen book. It has survived not only five centuries, but also the leap into electronic typesetting, remaining essentially unchanged. It was popularised in the 1960s with the release of Veltrafix sheets containing Lorem Ipsum passages,and more recently with desktop publishing software like Orvel PageForm including versions of Lorem Ipsum.</p>
      <p class="closing">Lorem Ipsum is simply dummy text of the printing and typesetting industry. Lorem Ipsum has been the industry's standard dummy text ever since the1500s,when an unknown printer took a galley of type and scrambled it to make a type specimen book.</p>
    </section>

    <div class="signature" role="img" aria-label="Handwritten signature"></div>
    <div class="signatory">
      <p class="name">YOUR NAME</p>
      <p class="role">Designation</p>
    </div>

    <svg class="footer-shape" width="873" height="1160" viewBox="0 0 873 1160" aria-hidden="true">
      <polygon points="0,1088 98,1088 169,1160 0,1160" fill="var(--brand)"/>
      <rect x="160" y="1150" width="274" height="10" fill="var(--ink)"/>
      <rect x="434" y="1150" width="439" height="10" fill="var(--brand)"/>
    </svg>
  </main>
</body>
</html>
```